Vortelan d.o.o. needes a web site design

We are a company dealing with automatic doors, industrial doors, roller shutters, access control systems.
We would like to get a design which is clean and neat, and here are some sites which work with similar products. These designs are some we like, but of course, I am looking for a design which is unique. We usually use grey and red colours, which you can see on www.vortelan.ba .
The sites we like are:
http://www.plexawin.com/gb/
http://www.brunosteca.it/eng/
http://faswoodportamel.com/

You have to understand, that we have 4 different groups of products, which are main groups. I would like if those 4 groups somehow could be in different colours. (Maybe "zuvex" colours), in order to separate the groups in some way.

Attached you have web site structure.

If any questions, please contact me.
Edvin

Target Market(s)

Bosnian market. Aluminium and PVC doors and window market, Construction companies, Supermarkets-Retail, Gas stations, Banks, Food industry, Heavy industry.

Industry/Entity Type

It Company

Contact Information for Business Card

I have attached our current business card in PDF. I weould like english on one side, bosnian on other side.

Logo Text

Vortelan is the name of the company, our core business is automation!

Number of Pages Required

5+ page

Font styles to use
Sans Serif

Colors
ec1f27
0792cd
9bcb3c
ffc214
ffffff

```html
<!DOCTYPE html>
<html lang="en">
<head>
<meta charset="utf-8">
<title>Vortelan d.o.o.</title>
<link href="https://fonts.googleapis.com/css2?family=Mulish:wght@400;600;700;800&family=Open+Sans:ital,wght@0,400;0,600;0,700;1,400&family=Oswald:wght@400;500&display=swap" rel="stylesheet">
<style>
:root{
  --red:#ec1f27;
  --red-btn:#d9303c;
  --footer-red:#d83a47;
  --blue:#0792cd;
  --green:#9bcb3c;
  --yellow:#ffc214;
  --white:#ffffff;
  --grey-text:#6b6b6b;
  --grey-dark:#4a4a4a;
  --ink:#111111;
  --submit:#3a3a3a;
}
*{box-sizing:border-box;margin:0;padding:0}
html,body{width:966px;height:1200px;overflow:hidden;background:var(--white)}
body{position:relative;font-family:"Open Sans",Arial,sans-serif}

.site-header{position:absolute;left:0;top:0;width:966px;height:91px;background:var(--white)}
.site-header .contact-line{position:absolute;top:37px;font-size:11px;color:var(--grey-text)}
.site-header .email{left:115px}
.site-header .phone{left:672px}
.brand{position:absolute;left:380px;top:26px;width:206px;display:flex;align-items:center;gap:8px}
.brand .mark{width:22px;height:22px;background:var(--red);flex:none}
.brand .name{font-family:"Mulish",sans-serif;font-weight:800;font-size:26px;color:var(--red);letter-spacing:1px}

.hero{position:absolute;left:0;top:91px;width:966px;height:474px;overflow:hidden}
.hero .hero-photo{position:absolute;inset:0;background:radial-gradient(ellipse at 50% 30%,#5a5a5a 0%,#3a3a3a 45%,#1a1a1a 100%)}
.hero h1{position:absolute;left:0;right:0;top:170px;text-align:center;font-family:"Mulish",sans-serif;font-weight:800;font-size:45px;color:var(--white);letter-spacing:1px}
.hero .lead{position:absolute;left:0;right:0;top:233px;text-align:center;font-family:"Open Sans",sans-serif;font-size:16px;line-height:23px;color:var(--white)}
.hero .btn{position:absolute;left:428px;top:301px;width:109px;height:34px;background:var(--red-btn);border:1px solid var(--white);border-radius:3px;color:var(--white);font-size:10px;display:flex;align-items:center;justify-content:center}
.hero .slider-nav{position:absolute;left:461px;top:450px;width:52px;height:24px;background:#d6d6d6;display:flex;align-items:center;justify-content:center;gap:9px}

.products-title{position:absolute;left:0;right:0;top:593px;text-align:center;font-family:"Mulish",sans-serif;font-weight:700;font-size:24px;color:var(--grey-dark)}
.products-title .accent{color:var(--red)}

.product{position:absolute;top:660px;width:211px;height:255px;display:flex;align-items:center;justify-content:center;text-align:center;font-family:"Oswald",sans-serif;font-size:30px;line-height:34px;color:var(--ink)}
.product.doors{left:40px;background:linear-gradient(160deg,#e23b3f,#d3232c)}
.product.shutters{left:267px;background:linear-gradient(180deg,#7a7a7a 0%,#555 25%,#6e6e6e 60%,#8f8f8f 88%,#b5b5b5 100%)}
.product.industrial{left:493px;background:linear-gradient(180deg,#9dcd43,#93c43a)}
.product.access{left:718px;background:linear-gradient(100deg,#e5b214 0%,#ffc730 40%,#ffcb35 100%)}
.product .more{position:absolute;left:0;bottom:0;width:100%;height:31px;background:var(--blue);color:var(--white);font-size:17px;display:flex;align-items:center;justify-content:center;gap:16px}

.site-footer{position:absolute;left:0;top:951px;width:966px;height:185px;background:var(--footer-red);color:var(--white)}
.site-footer h3{position:absolute;top:25px;font-family:"Open Sans",sans-serif;font-weight:600;font-size:14px;letter-spacing:.3px}
.about h3{left:38px}.contact h3{left:202px}.questions h3{left:525px}.follow h3{left:760px}
.footer-links{position:absolute;left:38px;top:56px;list-style:none}
.footer-links li{height:23px;display:flex;align-items:center;gap:8px;font-size:10px}
.form{position:absolute;left:206px;top:55px;width:255px}
.form .field{position:absolute;width:125px;height:32px;border:1px solid rgba(255,255,255,.85);font-size:10px;font-style:italic;color:rgba(255,255,255,.7);padding:9px 10px}
.form .submit{position:absolute;left:0;top:74px;width:105px;height:30px;background:var(--submit);color:var(--white);font-size:12px;display:flex;align-items:center;justify-content:center}
.questions ul{position:absolute;left:527px;top:56px;list-style:none}
.questions li{height:23px;display:flex;align-items:center;font-size:10px}
.social{position:absolute;left:757px;top:70px;display:flex;gap:8px}
.social span{width:28px;height:28px;border-radius:50%;background:var(--white)}

.copyright{position:absolute;left:0;top:1136px;width:966px;height:64px;background:#000;color:var(--white);font-size:10px;display:flex;align-items:center;justify-content:center}
</style>
</head>
<body>
<header class="site-header">
  <span class="contact-line email">Email id : info@companyname.com</span>
  <div class="brand"><span class="mark"></span><span class="name">vortelan d.o.o.</span></div>
  <span class="contact-line phone">Call Us : 123-456-7890</span>
</header>

<section class="hero">
  <div class="hero-photo" role="img" aria-label="Blurred black and white photo of people walking through an entrance hall"></div>
  <h1>NOVA WEB STRANICA</h1>
  <p class="lead">u toku su radovi na novoj web prezentaciji naših usluga,<br>uskoro smo ponovo sa vama</p>
  <span class="btn">READ MORE</span>
  <div class="slider-nav">
    <svg width="8" height="12" viewBox="0 0 8 12"><path d="M6 1 1 6l5 5" fill="none" stroke="#222" stroke-width="1.6"/></svg>
    <svg width="8" height="12" viewBox="0 0 8 12"><path d="M2 1l5 5-5 5" fill="none" stroke="#222" stroke-width="1.6"/></svg>
  </div>
</section>

<h2 class="products-title"><span class="accent">O</span>ur <span class="accent">P</span>roducts</h2>

<div class="product doors" role="img" aria-label="Red tinted photo of people passing through automatic glass doors">Automatic<br>Doors</div>
<div class="product shutters" role="img" aria-label="Photo of a closed metal roller shutter">
  <span class="more">READ MORE
    <svg width="26" height="26" viewBox="0 0 26 26"><circle cx="13" cy="13" r="11.5" fill="none" stroke="#fff" stroke-width="1.6"/><path d="M11 8l5 5-5 5" fill="none" stroke="#fff" stroke-width="2"/></svg>
  </span>
</div>
<div class="product industrial" role="img" aria-label="Green tinted photo of an industrial sectional door">Industrial<br>Doors</div>
<div class="product access" role="img" aria-label="Yellow tinted photo of a hand using a door access key">Access Control<br>Systems</div>

<footer class="site-footer">
  <div class="about">
    <h3>ABOUT US</h3>
    <ul class="footer-links">
      <li><svg width="12" height="12" viewBox="0 0 12 12"><circle cx="6" cy="6" r="5" fill="none" stroke="#fff" stroke-opacity=".7"/><path d="M5 3.5 7.5 6 5 8.5" fill="none" stroke="#fff" stroke-opacity=".7"/></svg>Home</li>
      <li><svg width="12" height="12" viewBox="0 0 12 12"><circle cx="6" cy="6" r="5" fill="none" stroke="#fff" stroke-opacity=".7"/><path d="M5 3.5 7.5 6 5 8.5" fill="none" stroke="#fff" stroke-opacity=".7"/></svg>Browse Activities</li>
      <li><svg width="12" height="12" viewBox="0 0 12 12"><circle cx="6" cy="6" r="5" fill="none" stroke="#fff" stroke-opacity=".7"/><path d="M5 3.5 7.5 6 5 8.5" fill="none" stroke="#fff" stroke-opacity=".7"/></svg>The Market</li>
      <li><svg width="12" height="12" viewBox="0 0 12 12"><circle cx="6" cy="6" r="5" fill="none" stroke="#fff" stroke-opacity=".7"/><path d="M5 3.5 7.5 6 5 8.5" fill="none" stroke="#fff" stroke-opacity=".7"/></svg>How it works</li>
      <li><svg width="12" height="12" viewBox="0 0 12 12"><circle cx="6" cy="6" r="5" fill="none" stroke="#fff" stroke-opacity=".7"/><path d="M5 3.5 7.5 6 5 8.5" fill="none" stroke="#fff" stroke-opacity=".7"/></svg>Blog</li>
    </ul>
  </div>
  <div class="contact">
    <h3>CONTACT US</h3>
    <div class="form">
      <span class="field" style="left:0;top:0">Name</span>
      <span class="field" style="left:129px;top:0">Phone</span>
      <span class="field" style="left:0;top:36px">E-mail</span>
      <span class="field" style="left:129px;top:36px">Message</span>
      <span class="submit">SUBMIT</span>
    </div>
  </div>
  <div class="questions">
    <h3>HAVE QUESTIONS?</h3>
    <ul>
      <li>123-456-7890</li>
      <li>Info@companyname.com</li>
      <li>Lorem Ipsum is simply dummy</li>
    </ul>
  </div>
  <div class="follow">
    <h3>FOLLOW US</h3>
    <div class="social"><span></span><span></span><span></span><span></span></div>
  </div>
</footer>

<div class="copyright">Copyright 2016 Company Name.&nbsp; All Rights Reserved.</div>
</body>
</html>
```